Business Card Design

Brambleton Energy, L.P. is an energy and lifecycle management firm that creates value in petroleum products through synergistic marketing, trading, recovery, logistics and beneficial reuse services.

Sell top-quality refinery feedstock, petroleum products and co-products on the spot and futures makets (energy trading)

Separate, reclaim and/or manufacture valuable products for beneficial reuse (environmental)
Updates

The tag line Understanding Solutions   Performance are three different concepts and need to be kept either spaced apart or separated in some way. Thanks. 

Target Market(s)

Refiners, Petroleum storage companies, energy marketers

Industry/Entity Type

Business

Contact Information for Business Card

Gwendolyn R. Hask
Principal
Brambleton Energy, L.P.
4817 Quillby St.
Houston, TX 77081
713-482-6619 phone
713-641-8854 fax
g.hask@brambletonenergy-example.com
www.brambletonenergy-example.com

Requirements
Must have
• Tagline outlined in matching orange -

Understanding Solutions Performance
Nice to have
• Coordinating typestyles

```html
<!DOCTYPE html>
<html lang="en">
<head>
<meta charset="utf-8">
<title>Brambleton Energy, L.P. — Business Card</title>
<link rel="stylesheet" href="https://fonts.googleapis.com/css2?family=Source+Sans+3:wght@400;600&display=swap">
<style>
  :root {
    --backdrop: #ececec;
    --card: #ffffff;
    --orange: #f26122;
    --orange-soft: #f5884e;
    --orange-text: #d9531e;
    --orange-name: #e8703a;
    --ink: #231f20;
    --white: #ffffff;
  }
  * { margin: 0; padding: 0; box-sizing: border-box; }
  html, body {
    width: 1200px; height: 1000px; overflow: hidden;
    background: var(--backdrop);
    font-family: "Source Sans 3", "Myriad Pro", sans-serif;
  }
  .card {
    position: absolute; left: 319px; top: 326px;
    width: 596px; height: 349px;
    background: var(--card);
    overflow: hidden;
  }
  .card-shapes { position: absolute; inset: 0; }
  .brand {
    position: absolute; left: 40px; top: 148px;
    display: flex; align-items: center; gap: 10px;
  }
  .brand-dot {
    width: 40px; height: 40px; border-radius: 50%;
    background: var(--ink);
  }
  .brand-name {
    font-weight: 600; font-size: 26px; line-height: 1;
    letter-spacing: 1px; text-transform: uppercase;
    color: var(--ink);
  }
  .tagline {
    position: absolute; left: 40px; top: 214px;
    display: flex; align-items: center; gap: 7px;
    padding: 4px 8px;
    border: 1px solid var(--orange);
    font-size: 10px; line-height: 1; letter-spacing: 0.6px;
    text-transform: uppercase; color: var(--orange-text);
  }
  .tagline-sep {
    width: 4px; height: 4px; border-radius: 50%;
    background: var(--orange);
  }
  .contact {
    position: absolute; left: 323px; top: 112px;
    font-size: 13.5px; line-height: 1.7;
    color: var(--orange-text);
  }
  .contact .contact-name { color: var(--orange-name); font-size: 14px; }
  .contact .contact-line { padding-left: 18px; white-space: nowrap; }
  .contact .contact-label { color: var(--orange-name); }
  .web {
    position: absolute; right: 8px; bottom: 7px;
    font-size: 16px; color: var(--white);
  }
</style>
</head>
<body>
  <div class="card">
    <svg class="card-shapes" width="596" height="349" viewBox="0 0 596 349">
      <g class="corner-band">
        <polygon points="0,0 28,0 0,36" fill="var(--orange-soft)"/>
        <polygon points="40,0 72,0 14,58 0,50" fill="var(--orange-soft)"/>
        <polygon points="84,0 154,0 0,124 0,80" fill="var(--orange-soft)"/>
      </g>
      <line class="divider" x1="312" y1="102" x2="312" y2="272"
            stroke="var(--orange)" stroke-width="2" stroke-dasharray="10 12"/>
      <polygon class="web-band" points="300,305 596,301 596,349 258,349" fill="var(--orange)"/>
    </svg>

    <div class="brand">
      <span class="brand-dot"></span>
      <span class="brand-name">Brambleton<br>Energy L.P.</span>
    </div>

    <div class="tagline">
      <span>Understanding</span><span class="tagline-sep"></span>
      <span>Solutions</span><span class="tagline-sep"></span>
      <span>Performance</span>
    </div>

    <div class="contact">
      <div class="contact-name">Gwendolyn R. Hask, Principal</div>
      <div class="contact-line">Brambleton Energy, L.P.</div>
      <div class="contact-line">4817 Quillby St., Houston, TX 77081</div>
      <div class="contact-line">713-482-6619 <span class="contact-label">phone</span></div>
      <div class="contact-line">713-641-8854 <span class="contact-label">fax</span></div>
      <div class="contact-line">g.hask@brambletonenergy-example.com</div>
    </div>

    <div class="web">www.brambletonenergy-example.com</div>
  </div>
</body>
</html>
```